LIFE CHANGING NEW WEBSITE DESIGN NEEDED FOR FULL WEBSITE- FUN/FEMININE!

I need a website designed for a personal financial advice website geared at women called LADY COIN MAVEN. I will be providing free financial advice around topics of making, saving, spending and sharing money. The concept is to change the way women understand money and the necessity around building various passive income streams to ensure full financial freedom. This will then carry down to advice for mothers with children and children in particular. The website should be elegant and yet witty. I don't want lots of serious photos but more relatable. I will have a photo of myself and my story as this is a blog and needs to be relatable to women and mothers. I like pinks and greys. I want to have a pink piggy bank being broken with a hammer in the front screen to break our traditional mindset around piggy bank saving/spending habits. I have created a logo that is a pink piggy head with LADY COIN MAVEN that needs to be incorporated so that it blends into the heading. I have also already started designing the website on Squarespace and can provide access to that. Basically it should have a format of LADY COIN MAVEN LOGO center in header then on left hand navigation: MAKE, SAVE, SPEND, SHARE then on right hand header navigation: MISSION, GET STARTED, CONTACT LCM I would like to have the front page when you go to the url to have the image of the piggy bank being broken then a catchy phrase then under 4 boxes with MAKE (image and description) SAVE (image and description) SPEND (image and description) SHARE (image and description) if you click on those or the title they go to pages that are dedicated to each them. Each page should have a little intro on the topic then I want lots of blog links as I will be mainly writing blogs. Each blog site should have ability to write comments as well. I need social media icons on each page too. Please let me know what you need from me to get started. I prefer having a discussion if possible to not waste anyone's time. I need the site to be easy for me to use and add blogs/urls etc as needed. I also need the site to be put into my domain that I already purchased: www.ladycoinmaven.example

Target Market(s)

teenage girls, 20 something girls, 30 something girls and mothers

Coding

Coded - Design and coding required

Number of Pages Required

5+ page

Font styles to use
Sans Serif

Colors
e667a6
e34197
f59195
eea4c8
aaaaaa
cbcbcb
959595

Requirements
Must have
• TOP NAVIGATION
• MAKE SAVE SPEND SHARE LOGO/LADY COIN MAVEN MISSION GET STARTED CONTACT LCM
• FRONT PAGE: IMAGE OF PIGGY BANK BEING BROKEN WITH A HAMMER
• CATCH PHRASE OVER THE IMAGE
• BUTTON IN PINK- TAKE ACTION (WHICH DIRECTS TO TAKE ACTION TAB ON NAVIGATION HEADER
• 4 BOXES BELOW MAIN IMAGE WITH IMAGE/DESCRIPTIONS FOR MAKE, SAVE, SPEND, SHARE THAT EACH GO TO THE PAGES FROM THE NAVIGATION HEADER
• EACH PAGE SHOULD BE DEDICATED TO THOSE TOPICS THEN THERE IS AN INTRO ON EACH PAGE THEN THE LINKS TO DIFFERENT BLOGS AROUND EACH TOPIC FOR MAKE, SAVE, SPEND, SHARE
• EACH BLOG SHOULD HAVE COMMENTS SECTION AND SOCIAL MEDIA ICONS
• (GOOD TO USE PINKS/GREYS)
Should not have
• BE SUPER BUSY, CLUTTERED, FEEL LIKE I AM SELLING SOMETHING

```html
<!DOCTYPE html>
<html lang="en">
<head>
<meta charset="utf-8">
<title>Lady Coin Maven</title>
<link href="https://fonts.googleapis.com/css2?family=Nunito:wght@400;600;700&family=Lato:wght@400;700&display=swap" rel="stylesheet">
<style>
:root{
  --pink:#e34197;
  --pink-soft:#e667a6;
  --coral:#f59195;
  --blush:#eea4c8;
  --grey-light:#cbcbcb;
  --grey:#aaaaaa;
  --grey-dark:#959595;
  --footer:#8a8a8a;
  --text:#555;
  --heading:#4a4a4a;
  --white:#fff;
}
*{margin:0;padding:0;box-sizing:border-box}
html,body{width:1200px;height:2434px;overflow:hidden}
body{font-family:'Nunito',sans-serif;color:var(--text);background:var(--white);position:relative}
a{text-decoration:none;color:inherit}

/* header */
.site-header{position:absolute;top:0;left:0;width:1200px;height:85px;background:var(--white);z-index:3}
.nav{position:absolute;top:35px;display:flex;gap:32px;font-size:16px;font-weight:600;color:#777;letter-spacing:.3px}
.nav-left{left:99px}
.nav-right{right:57px}
.brand-tab{position:absolute;left:466px;top:60px;width:268px;height:67px;background:var(--white);border-radius:0 0 60px 60px;z-index:3}
.brand{position:absolute;left:0;width:1200px;top:18px;text-align:center;z-index:4}
.brand-dot{display:block;width:40px;height:40px;border:3px solid var(--pink-soft);border-radius:50%;margin:0 auto 6px}
.brand-name{font-size:26px;font-weight:600;color:var(--pink)}

/* hero */
.hero{position:absolute;top:85px;left:0;width:1200px;height:573px;overflow:hidden;
  background:linear-gradient(180deg,#ee62a8 0%,#e2378a 50%,#cf1266 100%)}
.hero-photo{position:absolute;left:420px;top:0;width:780px;height:573px;
  background:
    radial-gradient(ellipse 130px 90px at 56% 58%, #f7d2dc 0%, rgba(247,210,220,0) 100%),
    radial-gradient(ellipse 210px 300px at 56% 78%, #3e78c4 0%, rgba(62,120,196,.75) 45%, rgba(62,120,196,0) 100%),
    radial-gradient(ellipse 120px 130px at 55% 22%, #f3d3a4 0%, rgba(243,211,164,.6) 50%, rgba(243,211,164,0) 100%),
    linear-gradient(90deg, rgba(238,98,168,0) 0%, rgba(240,130,188,.55) 35%, #f295c6 65%, #f3a6cd 100%)}
.hero-text{position:absolute;left:128px;top:130px;width:500px;text-align:center;color:var(--white)}
.hero-dot{display:block;width:40px;height:40px;border:3px solid var(--white);border-radius:50%;margin:0 auto 12px}
.hero-kicker{font-size:40px;font-weight:700;line-height:46px}
.hero-title{font-size:52px;font-weight:700;line-height:58px}
.hero-sub{font-size:19px;line-height:25px;margin-top:20px}
.btn{display:inline-block;background:var(--pink);color:var(--white);border-radius:30px;text-align:center;font-weight:600}
.btn-hero{background:var(--coral);width:192px;height:56px;line-height:56px;font-size:17px;margin-top:28px}
.arrow{position:absolute;top:242px}

/* topic cards */
.card{position:absolute;top:697px;width:220px;height:337px;border:2px solid var(--grey-light);background:var(--white);text-align:center}
.card-img{height:166px}
.card-title{font-size:21px;font-weight:600;color:var(--pink);margin-top:17px}
.card-text{font-size:12.5px;line-height:17px;margin:6px 14px 0;color:#666}
.btn-card{width:131px;height:38px;line-height:38px;font-size:13px;margin-top:16px}

/* mission */
.mission{position:absolute;top:1096px;left:0;width:1200px;height:509px;background:#e8e8e8}
.mission-photo{position:absolute;left:0;top:0;width:700px;height:509px;
  background:
    radial-gradient(ellipse 95px 110px at 68% 76%, #f48cc0 0%, rgba(244,140,192,.7) 60%, rgba(244,140,192,0) 100%),
    radial-gradient(ellipse 210px 170px at 28% 90%, #78cbc6 0%, rgba(120,203,198,.7) 55%, rgba(120,203,198,0) 100%),
    radial-gradient(ellipse 90px 110px at 34% 42%, #efc4a8 0%, rgba(239,196,168,0) 100%),
    radial-gradient(ellipse 190px 230px at 30% 35%, #8a5e3e 0%, rgba(138,94,62,.5) 55%, rgba(138,94,62,0) 100%),
    linear-gradient(90deg, #f1f1f1 0%, #f4f4f4 60%, rgba(232,232,232,0) 100%)}
.mission-body{position:absolute;left:612px;top:90px;width:475px}
.mission-title{font-size:36px;font-weight:700;color:var(--heading)}
.mission-text{font-size:16px;line-height:22px;margin:18px 0 0 3px}
.btn-mission{width:164px;height:48px;line-height:48px;font-size:16px;margin:28px 0 0 3px}

/* blog */
.section-title{position:absolute;left:162px;top:1668px;font-size:35px;font-weight:700;color:var(--pink)}
.meta{font-family:'Lato',sans-serif;font-size:14px;color:#555}
.post-title{font-family:'Lato',sans-serif;font-size:18px;font-weight:700;color:#333;line-height:24px;text-transform:uppercase}
.more{font-size:16px;font-weight:600;color:var(--coral)}
.feature{position:absolute;left:162px;top:1734px;width:429px}
.feature-img{height:243px;
  background:
    radial-gradient(ellipse 90px 80px at 33% 70%, #e9b8cc 0%, rgba(233,184,204,0) 100%),
    radial-gradient(ellipse 70px 70px at 72% 45%, #9a6a50 0%, rgba(154,106,80,0) 100%),
    radial-gradient(ellipse 160px 180px at 78% 40%, #2c201c 0%, rgba(44,32,28,.6) 60%, rgba(44,32,28,0) 100%),
    linear-gradient(90deg,#d9d9d9 0%,#c9c9c9 50%,#6b5244 100%)}
.feature-body{padding:34px 0 0 11px}
.feature .post-title{margin-top:10px}
.feature-text{font-family:'Lato',sans-serif;font-size:13px;line-height:22px;margin-top:10px;color:#555}
.feature .more{display:block;margin-top:14px}
.post{position:absolute;left:632px;width:416px;height:119px}
.post-img{position:absolute;left:0;top:0;width:128px;height:119px}
.post-body{position:absolute;left:157px;top:8px;width:260px}
.post-body .post-title{margin-top:5px}
.post-body .more{display:block;margin-top:10px}
.divider{position:absolute;left:632px;width:416px;height:1px;background:var(--grey)}

/* footer */
.site-footer{position:absolute;top:2258px;left:0;width:1200px;height:176px;background:var(--footer);color:var(--white);text-align:center}
.foot-nav{display:flex;justify-content:center;gap:30px;margin-top:43px;font-size:16px;font-weight:600}
.copy{font-size:13px;margin-top:14px}
.social{display:flex;justify-content:center;gap:34px;margin-top:24px}
.social a{width:22px;height:22px;border-radius:50%;border:2px solid var(--white);display:block}
</style>
</head>
<body>

<header class="site-header">
  <nav class="nav nav-left"><a href="#">MAKE</a><a href="#">SAVE</a><a href="#">SPEND</a><a href="#">SHARE</a></nav>
  <nav class="nav nav-right"><a href="#">MISSION</a><a href="#">GET STARTED</a><a href="#">CONTACT LCM</a></nav>
</header>
<div class="brand-tab"></div>
<div class="brand"><span class="brand-dot"></span><span class="brand-name">Lady Coin Maven</span></div>

<section class="hero">
  <div class="hero-photo" role="img" aria-label="Smiling blonde woman in a blue polka-dot shirt dropping a coin into a pink piggy bank"></div>
  <div class="hero-text">
    <span class="hero-dot"></span>
    <div class="hero-kicker">Welcome to</div>
    <div class="hero-title">Lady Coin Maven</div>
    <p class="hero-sub">Lorem ipsum dolor sit amet consectetuer<br>adipiscing elit Nam cursus Morbi</p>
    <a href="#" class="btn btn-hero">TAKE ACTION</a>
  </div>
  <svg class="arrow" style="left:58px" width="30" height="52" viewBox="0 0 30 52"><polyline points="27,2 3,26 27,50" fill="none" stroke="#fff" stroke-width="2.5"/></svg>
  <svg class="arrow" style="left:1102px" width="30" height="52" viewBox="0 0 30 52"><polyline points="3,2 27,26 3,50" fill="none" stroke="#fff" stroke-width="2.5"/></svg>
</section>

<article class="card" style="left:151px">
  <div class="card-img" role="img" aria-label="Hands typing on a laptop with banknotes flying" style="background:radial-gradient(ellipse 70px 60px at 75% 35%,#c9c6a8 0%,rgba(201,198,168,0) 100%),radial-gradient(ellipse 90px 50px at 40% 85%,#eeeeee 0%,rgba(238,238,238,0) 100%),linear-gradient(160deg,#d8cfcb 0%,#8b7f7a 55%,#3f3a38 100%)"></div>
  <h3 class="card-title">MAKE</h3>
  <p class="card-text">Lorem ipsum dolor sit amet consectetuer adipiscing elit Nam cursus Morbi ut mi Nullam</p>
  <a href="#" class="btn btn-card">CLICK HERE</a>
</article>
<article class="card" style="left:385px">
  <div class="card-img" role="img" aria-label="Hand placing a coin into a pink piggy bank" style="background:radial-gradient(ellipse 80px 60px at 45% 62%,#f3c2c3 0%,rgba(243,194,195,0) 100%),linear-gradient(135deg,#6a4a3c 0%,#b89488 45%,#e6e0dc 100%)"></div>
  <h3 class="card-title">SAVE</h3>
  <p class="card-text">Lorem ipsum dolor sit amet consectetuer adipiscing elit Nam cursus Morbi ut mi Nullam</p>
  <a href="#" class="btn btn-card">CLICK HERE</a>
</article>
<article class="card" style="left:618px">
  <div class="card-img" role="img" aria-label="Woman in sunglasses carrying shopping bags" style="background:radial-gradient(ellipse 60px 70px at 40% 75%,#f5c96a 0%,rgba(245,201,106,0) 100%),radial-gradient(ellipse 50px 60px at 60% 25%,#6a3b26 0%,rgba(106,59,38,0) 100%),linear-gradient(135deg,#f6e3bf 0%,#d9a36a 60%,#b47a4a 100%)"></div>
  <h3 class="card-title">SPEND</h3>
  <p class="card-text">Lorem ipsum dolor sit amet consectetuer adipiscing elit Nam cursus Morbi ut mi Nullam</p>
  <a href="#" class="btn btn-card">CLICK HERE</a>
</article>
<article class="card" style="left:851px">
  <div class="card-img" role="img" aria-label="Woman smiling at a laptop at home" style="background:radial-gradient(ellipse 70px 40px at 40% 80%,#d8d8d8 0%,rgba(216,216,216,0) 100%),radial-gradient(ellipse 60px 60px at 62% 55%,#2f8f92 0%,rgba(47,143,146,0) 100%),linear-gradient(135deg,#5a534c 0%,#9b948c 50%,#e0ddd8 100%)"></div>
  <h3 class="card-title">SHARE</h3>
  <p class="card-text">Lorem ipsum dolor sit amet consectetuer adipiscing elit Nam cursus Morbi ut mi Nullam</p>
  <a href="#" class="btn btn-card">CLICK HERE</a>
</article>

<section class="mission">
  <div class="mission-photo" role="img" aria-label="Curly-haired woman in a turquoise top saving money in a pink piggy bank"></div>
  <div class="mission-body">
    <h2 class="mission-title">Our Mission</h2>
    <p class="mission-text">My mission is simple- I want to challenge you to rethink the way you think about growing, spending and saving money. By redesigning your life around your finances I want you to run your life as if you are the CEO of your own business, and the business is maximising the value and profitability of your life.</p>
    <p class="mission-text" style="margin-top:24px">It is shocking that in today's world of information we are we still live in a society where most educated people leave school</p>
    <a href="#" class="btn btn-mission">LEARN MORE</a>
  </div>
</section>

<h2 class="section-title">Recent Blogs</h2>

<article class="feature">
  <div class="feature-img" role="img" aria-label="Smiling woman holding a piggy bank stuffed with banknotes"></div>
  <div class="feature-body">
    <div class="meta">April 12, 2019 &nbsp;|&nbsp; No Comments</div>
    <h3 class="post-title">Mauris vel lacus vitae felis vestibulum volutpat etiam est nunc</h3>
    <p class="feature-text">Nunc tempus felis vitae urna Vivamus porttitor neque at volutpat rutrum purus nisi eleifend libero a tempus libero lectus</p>
    <a href="#" class="more">Learn More</a>
  </div>
</article>

<article class="post" style="top:1734px">
  <div class="post-img" role="img" aria-label="Coin dropping into a white piggy bank" style="background:radial-gradient(ellipse 45px 35px at 60% 72%,#f4f1ee 0%,rgba(244,241,238,0) 100%),linear-gradient(135deg,#c98a4a 0%,#e0b07a 55%,#8e6a4a 100%)"></div>
  <div class="post-body">
    <div class="meta">April 08, 2019 &nbsp;|&nbsp; No Comments</div>
    <h3 class="post-title">Mauris vel lacus vitae felis vestibulum volutpat</h3>
    <a href="#" class="more">Learn More</a>
  </div>
</article>
<div class="divider" style="top:1870px"></div>
<article class="post" style="top:1893px">
  <div class="post-img" role="img" aria-label="Cupped hands holding a small white piggy bank" style="background:radial-gradient(ellipse 45px 40px at 45% 55%,#f6f2ee 0%,rgba(246,242,238,0) 100%),radial-gradient(ellipse 60px 30px at 45% 85%,#e8c6b0 0%,rgba(232,198,176,0) 100%),linear-gradient(135deg,#3f6f82 0%,#6a98a8 100%)"></div>
  <div class="post-body">
    <div class="meta">April 06, 2019 &nbsp;|&nbsp; No Comments</div>
    <h3 class="post-title">Fusce tellus sed metus augue convallis et</h3>
    <a href="#" class="more">Learn More</a>
  </div>
</article>
<div class="divider" style="top:2034px"></div>
<article class="post" style="top:2055px">
  <div class="post-img" role="img" aria-label="Mother and daughter with a pink piggy bank" style="background:radial-gradient(ellipse 30px 25px at 40% 80%,#f0b8cc 0%,rgba(240,184,204,0) 100%),radial-gradient(ellipse 45px 55px at 72% 30%,#4a3024 0%,rgba(74,48,36,0) 100%),linear-gradient(135deg,#e9e4de 0%,#c9b2a4 60%,#8a6a58 100%)"></div>
  <div class="post-body">
    <div class="meta">April 02, 2019 &nbsp;|&nbsp; No Comments</div>
    <h3 class="post-title">Phasellus felis dolor scelerisque a tempus</h3>
    <a href="#" class="more">Learn More</a>
  </div>
</article>

<footer class="site-footer">
  <nav class="foot-nav"><a href="#">MAKE</a><a href="#">SAVE</a><a href="#">SPEND</a><a href="#">SHARE</a><a href="#">MISSION</a><a href="#">GET STARTED</a><a href="#">CONTACT LCM</a></nav>
  <p class="copy">© 2019 Company Name &nbsp;All right reserved</p>
  <div class="social" aria-label="Social media links"><a href="#" aria-label="Social link 1"></a><a href="#" aria-label="Social link 2"></a><a href="#" aria-label="Social link 3"></a><a href="#" aria-label="Social link 4"></a></div>
</footer>

</body>
</html>
```